URGENT Christmas Greeting Card for IT Company

We URGENTLY need a Christmas Card for our clients. We are an IT Company that resell softwares from developers. We need the final design for Friday at the latest.

We are looking for a creative, yet elegant christmas card to give to our clients along with a gift. Please use our logo and the same color scheme.

Industry/Entity Type

It Company

Requirements
Must have
• Must have the logo and the colors of christmas and the company.
Nice to have
• I would like to see creative yet elegant designs, its a christmas card that a company is giving to its clients. It would be nice to see a modern, serious and elegant designs.

```html
<!DOCTYPE html>
<html lang="en">
<head>
<meta charset="utf-8">
<title>Merry Christmas &amp; Happy New Year</title>
<link href="https://fonts.googleapis.com/css2?family=Kaushan+Script&family=Raleway:wght@300;400;600;800&display=swap" rel="stylesheet">
<style>
  :root {
    --paper: #ffffff;
    --ink: #2b2b2b;
    --ink-soft: #444444;
    --amber: #f39a1e;
    --amber-deep: #d9621a;
    --ember: #e8312a;
    --silver: #9a9a9a;
    --silver-light: #d7d7d7;
  }
  * { margin: 0; padding: 0; box-sizing: border-box; }
  html, body {
    width: 1200px;
    height: 1200px;
    overflow: hidden;
    background: var(--paper);
  }
  .card {
    position: relative;
    width: 1200px;
    height: 1200px;
    background: var(--paper);
    font-family: "Raleway", sans-serif;
    color: var(--ink);
  }
  .festive-frame {
    position: absolute;
    inset: 0;
    width: 1200px;
    height: 1200px;
  }
  .greeting {
    position: absolute;
    left: 0;
    right: 0;
    text-align: center;
  }
  .greeting-merry {
    top: 392px;
    font-weight: 300;
    font-size: 58px;
    letter-spacing: 0.02em;
    line-height: 1;
    color: var(--ink);
  }
  .greeting-christmas {
    top: 452px;
    font-family: "Kaushan Script", cursive;
    font-size: 92px;
    line-height: 1;
    color: var(--ink);
    transform: rotate(-6deg);
    transform-origin: center;
  }
  .ornament {
    position: absolute;
    left: 576px;
    top: 552px;
    width: 48px;
    height: 62px;
  }
  .greeting-newyear {
    top: 628px;
    font-weight: 400;
    font-size: 23px;
    letter-spacing: 0.34em;
    padding-left: 0.34em;
    color: var(--ink-soft);
  }
  .dot-rule {
    position: absolute;
    left: 462px;
    top: 662px;
    width: 280px;
    height: 4px;
  }
  .brand {
    position: absolute;
    left: 0;
    right: 0;
    top: 742px;
    display: flex;
    justify-content: center;
    align-items: center;
    gap: 14px;
  }
  .brand-mark {
    width: 50px;
    height: 50px;
    border-radius: 50%;
    background: var(--ember);
    flex: none;
  }
  .brand-text {
    display: flex;
    flex-direction: column;
  }
  .brand-name {
    font-weight: 800;
    font-size: 44px;
    line-height: 1;
    letter-spacing: 0.01em;
    color: var(--ink);
  }
  .brand-tagline {
    font-weight: 800;
    font-size: 13.5px;
    letter-spacing: 0.03em;
    color: var(--ink);
    margin-top: 4px;
    text-transform: uppercase;
  }
</style>
</head>
<body>
  <main class="card">
    <svg class="festive-frame" viewBox="0 0 1200 1200" role="img" aria-label="Wreath-like border of faceted amber snowflakes, reindeer, Christmas trees and stars mixed with grey holly leaves, bells, music notes, hearts and paisley flowers, leaving a round clearing in the centre">
      <defs>
        <linearGradient id="frameTones" x1="0" y1="0" x2="1" y2="1">
          <stop offset="0" stop-color="#f6c27a"/>
          <stop offset="0.35" stop-color="#e4e4e4"/>
          <stop offset="0.65" stop-color="#f3b467"/>
          <stop offset="1" stop-color="#dcdcdc"/>
        </linearGradient>
        <radialGradient id="clearingFade" cx="600" cy="620" r="420" gradientUnits="userSpaceOnUse">
          <stop offset="0.7" stop-color="#ffffff" stop-opacity="0.55"/>
          <stop offset="1" stop-color="#ffffff" stop-opacity="0"/>
        </radialGradient>
      </defs>
      <path fill="url(#frameTones)" fill-rule="evenodd"
            d="M60 60 H1140 V1140 H60 Z M600 320 a300 300 0 1 0 0.1 0 Z"/>
      <rect x="60" y="60" width="1080" height="1080" fill="url(#clearingFade)"/>
    </svg>

    <h1 class="greeting greeting-merry">MERRY</h1>
    <p class="greeting greeting-christmas">Christmas</p>

    <svg class="ornament" viewBox="0 0 48 62" aria-hidden="true">
      <line x1="24" y1="0" x2="24" y2="8" stroke="#2b2b2b" stroke-width="1.5" stroke-dasharray="2 2"/>
      <rect x="20" y="8" width="8" height="6" rx="1.5" fill="#2b2b2b"/>
      <circle cx="24" cy="37" r="23" fill="#f39a1e"/>
      <text x="24" y="46" text-anchor="middle" font-family="Kaushan Script, cursive" font-size="26" fill="#ffffff">&amp;</text>
    </svg>

    <p class="greeting greeting-newyear">HAPPY NEW YEAR</p>

    <svg class="dot-rule" viewBox="0 0 280 4" aria-hidden="true">
      <line x1="2" y1="2" x2="278" y2="2" stroke="#444444" stroke-width="3" stroke-linecap="round" stroke-dasharray="0 17.25"/>
    </svg>

    <div class="brand">
      <span class="brand-mark" aria-hidden="true"></span>
      <div class="brand-text">
        <span class="brand-name">NEXORIA</span>
        <span class="brand-tagline">IT Consulting and Services</span>
      </div>
    </div>
  </main>
</body>
</html>
```